Korvane Plumbing Business cards

Company is Korvane Plumbing.
name Dorian Malvessey, I am a plumber, drainer, gasfitter and roofer
Mobile: 0461 590 314
Email address: info@korvaneplumbing.example (check out my website for some ideas)
Website: www.korvaneplumbing.example
ABN: 42 198 603 771
LIC: 516042D

I am reliable all round plumber. I am a 24 hour emergency service. Korvane Plumbing is a professional plumbing service in the Illawarra, South Coast, Southern Sydney and Southern Highland regions of NSW. We offer a 24 hour emergency service for piece of mind to our customers. Call us now to see how we can help you. Korvane Plumbing approaches every job with attention to detail and excellent customer service. With our superior workmanship you can be confident that the job will be done right the first time around. You can rest assured with results that are guaranteed to last.

Target Market(s)

the general public

Contact Information for Business Card

look up website for some ideas something with similar colours to logo and new modern and to catch the eye.

Colors
fdfdfd
ffffff
000000
7f7f7f
aaaaaa
33a6d7
0492cd

Requirements
Must have
• all contact details
• company- Korvane Plumbing
• name- Dorian Malvessey
• number mobile- 0461 590 314
• Email address- info@korvaneplumbing.example
• Website- www.korvaneplumbing.example
• ABN- 42 198 603 771
• LIC- 516042D

```html
<!DOCTYPE html>
<html lang="en">
<head>
<meta charset="utf-8">
<title>Korvane Plumbing Business Cards</title>
<link href="https://fonts.googleapis.com/css2?family=Roboto:wght@300;400;700&display=swap" rel="stylesheet">
<style>
  :root {
    --backdrop: #1c2431;
    --card: #0f0f10;
    --blue: #1a9ad0;
    --blue-light: #33a6d7;
    --grey: #7f7f7f;
    --grey-light: #aaaaaa;
    --white: #fdfdfd;
    --divider: #222326;
  }
  * { box-sizing: border-box; margin: 0; padding: 0; }
  html, body { width: 1200px; height: 1200px; overflow: hidden; }
  body {
    background: var(--backdrop);
    font-family: "Roboto", Arial, sans-serif;
    position: relative;
  }
  .card {
    position: absolute;
    left: 170px;
    width: 860px;
    height: 480px;
    background: var(--card);
    border-bottom: 4px solid var(--blue);
    box-shadow: 0 18px 40px rgba(0,0,0,.45);
  }
  .card--front { top: 90px; }
  .card--back { top: 630px; }

  /* front */
  .brand {
    position: absolute;
    left: 60px;
    top: 0;
    width: 330px;
    height: 100%;
    display: flex;
    align-items: center;
    gap: 18px;
  }
  .brand__mark {
    width: 40px; height: 40px;
    border-radius: 50%;
    background: var(--grey);
    flex: none;
  }
  .brand__name {
    color: var(--blue);
    font-weight: 700;
    font-size: 40px;
    line-height: 1.05;
    letter-spacing: 2px;
    text-transform: uppercase;
  }
  .divider {
    position: absolute;
    left: 410px;
    top: 120px;
    width: 1px;
    height: 230px;
    background: var(--divider);
  }
  .details {
    position: absolute;
    left: 450px;
    top: 130px;
    right: 30px;
  }
  .details__name {
    color: var(--blue);
    font-size: 34px;
    font-weight: 400;
    text-transform: uppercase;
    letter-spacing: .5px;
  }
  .details__role {
    color: var(--grey);
    font-size: 17px;
    font-weight: 300;
    margin-top: 4px;
  }
  .contact {
    list-style: none;
    margin-top: 18px;
  }
  .contact__item {
    display: flex;
    align-items: center;
    gap: 16px;
    color: var(--white);
    font-size: 22px;
    font-weight: 400;
    height: 42px;
  }
  .contact__item--phone {
    font-weight: 700;
    letter-spacing: 4px;
    font-size: 26px;
  }
  .contact__icon { width: 24px; height: 24px; flex: none; }

  /* back */
  .back-brand {
    position: absolute;
    left: 0; right: 0;
    top: 120px;
    display: flex;
    flex-direction: column;
    align-items: center;
    gap: 22px;
  }
  .back-brand__mark {
    width: 56px; height: 56px;
    border-radius: 50%;
    background: var(--grey);
  }
  .back-brand__name {
    color: var(--blue);
    font-weight: 700;
    font-size: 46px;
    letter-spacing: 3px;
    text-transform: uppercase;
  }
  .registration {
    position: absolute;
    left: 0; right: 0;
    top: 320px;
    text-align: center;
    color: var(--white);
    font-size: 26px;
    letter-spacing: 5px;
    line-height: 1.45;
  }
</style>
</head>
<body>
  <section class="card card--front">
    <div class="brand">
      <span class="brand__mark"></span>
      <span class="brand__name">Korvane<br>Plumbing</span>
    </div>
    <div class="divider"></div>
    <div class="details">
      <h1 class="details__name">Dorian Malvessey</h1>
      <p class="details__role">I am a plumber, drainer, gasfitter and roofer</p>
      <ul class="contact">
        <li class="contact__item contact__item--phone">
          <svg class="contact__icon" viewBox="0 0 24 24" aria-hidden="true"><rect x="6" y="2" width="12" height="20" rx="2" fill="none" stroke="var(--blue)" stroke-width="2"/><circle cx="12" cy="18" r="1.2" fill="var(--blue)"/></svg>
          0461 590 314
        </li>
        <li class="contact__item">
          <svg class="contact__icon" viewBox="0 0 24 24" aria-hidden="true"><rect x="2" y="5" width="20" height="14" rx="1.5" fill="var(--blue)"/><path d="M3 6l9 7 9-7" fill="none" stroke="var(--card)" stroke-width="1.6"/></svg>
          info@korvaneplumbing.example
        </li>
        <li class="contact__item">
          <svg class="contact__icon" viewBox="0 0 24 24" aria-hidden="true" fill="none" stroke="var(--blue)" stroke-width="1.4"><circle cx="12" cy="12" r="10"/><ellipse cx="12" cy="12" rx="4.5" ry="10"/><path d="M2 12h20M4 7h16M4 17h16"/></svg>
          www.korvaneplumbing.example
        </li>
      </ul>
    </div>
  </section>

  <section class="card card--back">
    <div class="back-brand">
      <span class="back-brand__mark"></span>
      <span class="back-brand__name">Korvane Plumbing</span>
    </div>
    <p class="registration">LIC: 516042D<br>ABN: 42 198 603 771</p>
  </section>
</body>
</html>
```